MOLT - Monitoring Natural Hazards from Space Web Application

KORVEN Sarl is a Luxembourg based Space-Startup that works in the field of Earth Observation. KORVEN is a platform able to extract value-added information from satellite data and is specialized in mapping Natural Disaster (floods, fires etc).

We are now developing a new vertical tool, called MOLT, dedicated to the monitoring of natural hazards in Humanitarian Camps around the world.

The goal of MOLT is to hide to the users' all the complexity of the Satellite Image processing and just provide them the results.

This project require to Design 4 pages of MOLT:
• Public Home Page (Code - V01)
• Dashboard (private Home Page) (Code - V03)
• Monitor (web GIS) (Code - V14)
• Registration Page (Code - V04)

We would like to provide the required time to make a good job.

Target Market(s)

Humanitarian Agencies, Goverments

Coding

Coded - Design and coding required

Number of Pages Required

4 page

Font styles to use
Other font styles liked:
• see the manual attached

Requirements
Must have
• 4 pages. One Home, one form, one dashboard and one web map.
Nice to have
• Please read the attachment with all the detailed instructions

```html
<!DOCTYPE html>
<html lang="en">
<head>
<meta charset="utf-8">
<title>Register to MOLT</title>
<link href="https://fonts.googleapis.com/css2?family=Outfit:wght@300;400;500;600&family=Space+Mono:wght@700&display=swap" rel="stylesheet">
<style>
  :root {
    --navy: #264b58;
    --ink: #1f3f4b;
    --line: #6d8791;
    --gold: #eeb840;
    --page: #eff1f2;
    --white: #ffffff;
    --muted: #4c5e66;
  }
  * { box-sizing: border-box; margin: 0; padding: 0; }
  html, body { width: 1200px; height: 999px; overflow: hidden; }
  body {
    position: relative;
    font-family: "Outfit", sans-serif;
    color: var(--ink);
    background:
      radial-gradient(ellipse 170px 330px at 0px 560px, rgba(120,145,158,0.75), rgba(120,145,158,0) 100%),
      radial-gradient(ellipse 150px 340px at 1200px 300px, rgba(238,190,90,0.6), rgba(238,190,90,0) 100%),
      var(--page);
  }
  .brand {
    position: absolute; top: 23px; left: 457px;
    display: flex; align-items: center; gap: 26px;
  }
  .brand-dot {
    width: 70px; height: 70px; border-radius: 50%;
    border: 2px solid var(--gold);
  }
  .brand-name {
    font-family: "Outfit", sans-serif; font-weight: 300;
    font-size: 54px; letter-spacing: 14px; color: var(--navy);
  }
  .card {
    position: absolute; left: 124px; top: 127px;
    width: 961px; height: 729px;
    background: var(--white); border-radius: 31px;
  }
  .title {
    position: absolute; top: 30px; left: 0; width: 100%;
    text-align: center;
    font-family: "Space Mono", monospace; font-weight: 700;
    font-size: 40px; letter-spacing: 3px; color: var(--navy);
  }
  .title .accent { color: var(--gold); }
  .title-rule {
    position: absolute; top: 80px; left: 453px;
    width: 65px; height: 2px; background: var(--gold);
  }
  .spark { position: absolute; top: 18px; left: 680px; width: 22px; height: 22px; }
  .label {
    position: absolute; font-size: 16px; font-weight: 400; color: var(--ink);
    line-height: 18px;
  }
  .hint {
    position: absolute; font-size: 9.5px; line-height: 12px;
    text-align: right; color: var(--ink);
  }
  .field {
    position: absolute; height: 44px;
    border: 1px solid var(--line); border-radius: 2px;
    background: var(--white);
    display: flex; align-items: center; justify-content: space-between;
    padding: 0 16px;
    font-size: 13px; font-weight: 300; color: var(--ink);
  }
  .field svg { width: 14px; height: 14px; }
  .check {
    position: absolute; left: 72px;
    display: flex; align-items: center; gap: 7px;
    font-size: 12px; font-weight: 300; color: var(--muted);
  }
  .check .box {
    width: 21px; height: 19px; border: 1.5px solid var(--navy); border-radius: 2px;
  }
  .check b { font-weight: 600; color: var(--ink); }
  .register {
    position: absolute; left: 68px; top: 641px;
    width: 178px; height: 48px;
    background: var(--gold); border-radius: 2px;
    display: flex; align-items: center; justify-content: center; gap: 8px;
    font-size: 18px; font-weight: 500; color: var(--navy);
  }
  .register svg { width: 12px; height: 14px; }
  .footer {
    position: absolute; left: 0; top: 925px; width: 1200px; height: 74px;
    background: var(--navy);
    display: flex; align-items: center; justify-content: center;
    color: var(--white); font-size: 15px; font-weight: 500; letter-spacing: 0.3px;
  }
</style>
</head>
<body>
  <header class="brand">
    <div class="brand-dot"></div>
    <div class="brand-name">MOLT</div>
  </header>

  <main class="card">
    <h1 class="title">REGISTER TO <span class="accent">MOLT</span></h1>
    <svg class="spark" viewBox="0 0 20 20"><path d="M10 0 L12 8 L20 10 L12 12 L10 20 L8 12 L0 10 L8 8 Z" fill="#eeb840"/></svg>
    <div class="title-rule"></div>

    <!-- account column -->
    <div class="label" style="left:70px;top:109px">User Id</div>
    <div class="hint" style="left:300px;top:120px;width:120px">At least 8 characters</div>
    <div class="field" style="left:69px;top:137px;width:388px"></div>

    <div class="label" style="left:69px;top:199px">Password</div>
    <div class="hint" style="left:190px;top:195px;width:230px">At least 8 characters that mix at least one char,<br>one number and one special symbol.</div>
    <div class="field" style="left:68px;top:225px;width:388px"></div>

    <div class="label" style="left:69px;top:285px">Confirm Password</div>
    <div class="field" style="left:68px;top:310px;width:388px"></div>

    <div class="label" style="left:72px;top:369px">Name</div>
    <div class="label" style="left:252px;top:369px">Surname</div>
    <div class="field" style="left:70px;top:394px;width:187px">First Name</div>
    <div class="field" style="left:268px;top:394px;width:187px">Last Name</div>

    <div class="label" style="left:72px;top:455px">Mobile Number</div>
    <div class="field" style="left:72px;top:481px;width:384px"></div>

    <div class="check" style="top:549px"><span class="box"></span><span>I have read and Accept the <b>MOLT</b> Terms and Conditions</span></div>
    <div class="check" style="top:582px"><span class="box"></span><span>I have read and Accept the <b>MOLT</b> Privacy Policy</span></div>

    <div class="register">REGISTER
      <svg viewBox="0 0 12 14"><path d="M3 2 L9 7 L3 12" fill="none" stroke="#264b58" stroke-width="2"/></svg>
    </div>

    <!-- organization column -->
    <div class="label" style="left:498px;top:115px">E-mail</div>
    <div class="field" style="left:495px;top:140px;width:389px"></div>

    <div class="label" style="left:493px;top:202px">Confirm E-mail</div>
    <div class="field" style="left:494px;top:228px;width:389px"></div>

    <div class="label" style="left:495px;top:285px">Organization Name</div>
    <div class="field" style="left:494px;top:313px;width:389px"></div>

    <div class="label" style="left:494px;top:368px">Organization Type</div>
    <div class="field" style="left:493px;top:396px;width:389px">Select Organization
      <svg viewBox="0 0 14 14"><path d="M2 4 L7 9 L12 4" fill="none" stroke="#264b58" stroke-width="2"/></svg>
    </div>

    <div class="label" style="left:496px;top:456px">Organization Address</div>
    <div class="field" style="left:494px;top:482px;width:192px">Street</div>
    <div class="field" style="left:694px;top:482px;width:192px">Number</div>
    <div class="field" style="left:494px;top:535px;width:192px">Postal Code</div>
    <div class="field" style="left:694px;top:534px;width:192px">City</div>
    <div class="field" style="left:495px;top:590px;width:192px">Phone</div>
    <div class="field" style="left:695px;top:589px;width:192px">Select Country
      <svg viewBox="0 0 14 14"><path d="M2 4 L7 9 L12 4" fill="none" stroke="#264b58" stroke-width="2"/></svg>
    </div>
  </main>

  <footer class="footer">Copyright © 2024 Molt. All Right Reserved</footer>
</body>
</html>
```